Posters to advertise a jewellery design school

I would like two pieces of artwork designing for our jewellery design school in Kuala Lumpur Malaysia.
60cm by 180cm poster
100cm by 100cm poster

My personal style is ‘perfectly imperfect’ but we wold like to show that we give quality classes in a fun and artistic / creative environment

The posters must contain our logo and you can choose to use as many or as few images as you like to tell the story or even include hand drawn line images.

https://files.brambleshare.net/folders/7kQzWmR2pLxT8nYv__HbS3dFj6cNa9Ec?usp=sharing

Please include the following wording on the poster
So you want to be a jewellery designer?

Part time and full-time classes available in:
Silversmithing
Jewellery design and rendering
Stone setting
Gemmology
Enamelling
Computer aided design
60cm by 180cm poster
100cm by 100cm poster

The posters must contain our logo and you can choose to use as many or as few images as you like to tell the story.

Silversmithing
Stone setting
Gemmology
Enamelling
Computer aided design

60cm by 180cm poster
100cm by 100cm poster

Silversmithing
Stone setting
Gemmology
Enamelling
Computer aided design

```html
<!DOCTYPE html>
<html lang="en">
<head>
<meta charset="utf-8">
<title>Mara Quinn Jewellery – Jewellery Design Classes</title>
<link rel="stylesheet" href="https://fonts.googleapis.com/css2?family=Poppins:wght@300;700&family=Questrial&display=swap">
<style>
  :root {
    --teal: #0c7273;
    --ink: #4a4a4c;
    --ink-soft: #5c5c5e;
    --paper: #ffffff;
    --mist: #eef1f2;
  }
  * { margin: 0; padding: 0; box-sizing: border-box; }
  html, body { width: 1200px; height: 1200px; overflow: hidden; background: var(--paper); }
  .poster {
    position: relative;
    width: 1200px;
    height: 1200px;
    overflow: hidden;
    background: radial-gradient(ellipse at 30% 35%, var(--paper) 0%, var(--mist) 55%, #f7f9f9 100%);
    font-family: "Questrial", sans-serif;
    color: var(--ink);
  }
  .brand {
    position: absolute;
    left: 58px;
    top: 70px;
    width: 240px;
    text-align: center;
  }
  .brand-mark {
    display: block;
    width: 92px;
    height: 92px;
    margin: 0 auto 18px;
    border: 5px solid var(--ink-soft);
    border-radius: 50%;
  }
  .brand-name {
    font-size: 31px;
    letter-spacing: 1px;
    color: var(--ink);
    line-height: 1;
  }
  .brand-sub {
    font-size: 18px;
    letter-spacing: 2px;
    color: var(--ink);
    margin-top: 8px;
  }
  .headline { position: absolute; left: 0; top: 0; width: 470px; }
  .headline-lead {
    position: absolute;
    left: 190px;
    top: 326px;
    font-size: 31px;
    line-height: 34px;
    white-space: nowrap;
  }
  .headline-lead .hl {
    background: var(--teal);
    color: var(--paper);
    padding: 0 4px;
  }
  .headline-lead .tail { color: var(--ink); margin-left: 4px; }
  .headline-main {
    position: absolute;
    left: 64px;
    top: 340px;
    font-family: "Poppins", sans-serif;
    font-weight: 300;
    font-size: 112px;
    letter-spacing: -4px;
    color: var(--ink);
    line-height: 1;
  }
  .headline-accent {
    position: absolute;
    left: 106px;
    top: 432px;
    font-family: "Poppins", sans-serif;
    font-weight: 700;
    font-size: 70px;
    letter-spacing: -1px;
    color: var(--teal);
    line-height: 1;
  }
  .offer-band {
    position: absolute;
    left: 0;
    width: 455px;
    height: 31px;
    background: var(--teal);
    color: var(--paper);
    font-size: 30px;
    line-height: 31px;
    text-align: right;
    padding-right: 4px;
    white-space: nowrap;
  }
  .offer-band.first { top: 549px; }
  .offer-band.second { top: 584px; }
  .course-list {
    position: absolute;
    left: 66px;
    top: 644px;
    list-style: none;
  }
  .course-list li {
    position: relative;
    padding-left: 40px;
    font-size: 30px;
    line-height: 43px;
    color: var(--ink-soft);
    white-space: nowrap;
  }
  .course-list li::before {
    content: "";
    position: absolute;
    left: 0;
    top: 12px;
    border-left: 20px solid var(--teal);
    border-top: 11px solid transparent;
    border-bottom: 11px solid transparent;
  }
  .feature, .gallery { position: absolute; left: 0; top: 0; }
</style>
</head>
<body>
<main class="poster">
  <div class="brand">
    <span class="brand-mark"></span>
    <div class="brand-name">MARA QUINN</div>
    <div class="brand-sub">jewellery</div>
  </div>

  <h1 class="headline">
    <span class="headline-lead"><span class="hl">you want to be</span><span class="tail">a</span></span>
    <span class="headline-main">jewellery</span>
    <span class="headline-accent">designer?</span>
  </h1>

  <div class="offer-band first">Part time and full-time</div>
  <div class="offer-band second">classes available in:</div>

  <ul class="course-list">
    <li>Silversmithing</li>
    <li>Jewellery design &amp; rendering</li>
    <li>Stone setting</li>
    <li>Gemmology</li>
    <li>Enamelling</li>
    <li>Computer aided design</li>
  </ul>

  <svg class="feature" width="1200" height="1200" viewBox="0 0 1200 1200">
    <defs>
      <linearGradient id="featureTone" x1="0" y1="0" x2="1" y2="1">
        <stop offset="0" stop-color="#b07a55"/>
        <stop offset="0.3" stop-color="#3a3a3c"/>
        <stop offset="0.6" stop-color="#1e1e20"/>
        <stop offset="0.85" stop-color="#4a7f95"/>
        <stop offset="1" stop-color="#2a2a2c"/>
      </linearGradient>
    </defs>
    <path class="feature-frame" d="M1200,4 C1000,90 760,250 678,396 C760,600 980,820 1200,952" fill="none" stroke="var(--teal)" stroke-width="3"/>
    <path class="feature-photo" role="img" aria-label="Close-up photograph of handmade rings, a pendant and an opal necklace on a dark workbench"
      d="M1048,84 C900,170 720,320 684,396 C760,560 880,700 976,792 C1060,680 1140,600 1200,520 L1200,470 C1160,300 1100,180 1048,84 Z" fill="url(#featureTone)"/>
    <path class="feature-wedge" d="M1048,84 C1100,180 1160,300 1200,470 L1200,8 C1150,35 1100,58 1048,84 Z" fill="var(--teal)"/>
    <path class="feature-wedge" d="M976,792 C1060,680 1140,600 1200,520 L1200,940 C1120,890 1040,845 976,792 Z" fill="var(--teal)"/>
  </svg>

  <svg class="gallery" width="1200" height="1200" viewBox="0 0 1200 1200">
    <defs>
      <linearGradient id="toneWorkshop" x1="0" y1="0" x2="1" y2="1">
        <stop offset="0" stop-color="#8b8986"/><stop offset="0.5" stop-color="#c9b79d"/><stop offset="1" stop-color="#5a4e44"/>
      </linearGradient>
      <linearGradient id="toneBangles" x1="0" y1="0" x2="1" y2="1">
        <stop offset="0" stop-color="#c9c6c0"/><stop offset="0.5" stop-color="#c9a840"/><stop offset="1" stop-color="#3f6a52"/>
      </linearGradient>
      <linearGradient id="toneCollection" x1="0" y1="0" x2="1" y2="1">
        <stop offset="0" stop-color="#e9e7e4"/><stop offset="0.5" stop-color="#d4a285"/><stop offset="1" stop-color="#f1efec"/>
      </linearGradient>
      <linearGradient id="toneStudents" x1="0" y1="0" x2="1" y2="1">
        <stop offset="0" stop-color="#6e7478"/><stop offset="0.5" stop-color="#d8d2cb"/><stop offset="1" stop-color="#2c2f3a"/>
      </linearGradient>
    </defs>
    <polygon role="img" aria-label="Student working at a jeweller's bench with a microscope" points="100,992 348,992 296,1200 36,1200" fill="url(#toneWorkshop)"/>
    <polygon role="img" aria-label="Row of silver bangles set with gold bezels and gemstones" points="356,992 646,992 594,1200 304,1200" fill="url(#toneBangles)"/>
    <polygon role="img" aria-label="Collection of student-made necklaces, earrings and a copper cuff" points="654,992 944,992 892,1200 602,1200" fill="url(#toneCollection)"/>
    <polygon role="img" aria-label="Group of students in aprons in the studio" points="952,992 1200,992 1200,1200 900,1200" fill="url(#toneStudents)"/>
  </svg>
</main>
</body>
</html>
```